DMB - Stationery Design Project

We need stationery based on our logo.

Company info :
Cabinet Durvaux & Associés
Société à responsabilité limitée au capital de 200.000 FCFP
RCS Papeete 58207K - Numéro tahiti K63095
Centre d’affaires OPALE - Rue Gaston Verdier
BP 51839 MAHANA KOLO - 98799 Motu Ravea
Tahiti - Polynésie française
Tél : +689 00 00 01 11
Fax : +689 00 00 01 12

Industry/Entity Type

It Company

Font styles to use
Sans Serif

```html
<!DOCTYPE html>
<html lang="fr">
<head>
<meta charset="utf-8">
<title>DMB – Enveloppes</title>
<link rel="stylesheet" href="https://fonts.googleapis.com/css2?family=Jost:wght@300;400&display=swap">
<style>
  :root {
    --backdrop: #e4e5e7;
    --paper: #ffffff;
    --navy: #1b3358;
    --slate: #6d7785;
    --rule: #9aa1ab;
    --ghost: #eceef1;
  }
  * { margin: 0; padding: 0; box-sizing: border-box; }
  html, body { width: 1200px; height: 1000px; overflow: hidden; }
  body {
    background: var(--backdrop);
    font-family: "Jost", sans-serif;
    color: var(--navy);
    position: relative;
  }
  .envelope {
    position: absolute;
    left: 230px;
    width: 740px;
    height: 370px;
    background: var(--paper);
    box-shadow: 0 2px 6px rgba(0,0,0,0.12);
    overflow: hidden;
  }
  .envelope--back { top: 70px; }
  .envelope--front { top: 540px; }

  .flap {
    position: absolute;
    left: 0; top: 0;
    width: 100%;
    height: 120px;
    background: var(--navy);
    border-radius: 0 0 14px 14px;
    box-shadow: 0 3px 6px rgba(0,0,0,0.25);
  }
  .back-mark {
    position: absolute;
    right: 40px;
    top: 150px;
    text-align: right;
  }
  .back-mark .wordmark { font-size: 30px; font-weight: 300; letter-spacing: 1px; line-height: 1; }
  .back-mark .tagline { font-size: 6px; color: var(--slate); margin-top: 3px; letter-spacing: 0.3px; }

  .sender {
    position: absolute;
    left: 34px;
    top: 34px;
    width: 300px;
  }
  .sender .wordmark {
    font-size: 52px;
    font-weight: 300;
    letter-spacing: 2px;
    line-height: 1;
  }
  .sender .firm {
    font-size: 12px;
    color: var(--slate);
    margin-top: 4px;
    letter-spacing: 0.3px;
  }
  .sender .divider {
    height: 1px;
    background: var(--rule);
    margin: 8px 0 6px;
  }
  .sender .address {
    font-size: 7px;
    color: var(--slate);
    line-height: 1.6;
    letter-spacing: 0.1px;
    white-space: nowrap;
  }
  .ghost-mark {
    position: absolute;
    right: 40px;
    top: 110px;
    font-size: 150px;
    font-weight: 300;
    letter-spacing: 8px;
    color: var(--ghost);
    line-height: 1;
  }
</style>
</head>
<body>
  <section class="envelope envelope--back" aria-label="Enveloppe, verso">
    <div class="flap"></div>
    <div class="back-mark">
      <div class="wordmark">DMB</div>
      <div class="tagline">Cabinet Durvaux &amp; Associés</div>
    </div>
  </section>

  <section class="envelope envelope--front" aria-label="Enveloppe, recto">
    <div class="sender">
      <div class="wordmark">DMB</div>
      <div class="firm">Cabinet Durvaux &amp; Associés</div>
      <div class="divider"></div>
      <p class="address">Centre d’affaires OPALE - Rue Gaston Verdier BP 51839 MAHANA KOLO - 98799 Motu Ravea<br>
      Tél : +689 00 00 01 11 - Fax : +689 00 00 01 12</p>
    </div>
    <div class="ghost-mark" aria-hidden="true">DMB</div>
  </section>
</body>
</html>
```